Business Card Design Project

I own a dental practice and would like to use a logo that was recently designed to make business cards.
I am looking for a clean card with the following information on the card.

Halvorsen Dental Center (Using the logo)
Martin K. Halvorsen, D.D.S.
2847 Willow Bend Rd. Suite B
Colorado Springs, CO 80471
(719) 555-0186
halvorsendentalcenter@mailnest.example
www.halvorsendentalcenter.example

Also a list of items on the back:
Services include

Family Dentistry
Cosmetic
Whitening
Tooth Colored Fillings
Crowns/Bridges
Implants/Tooth Replacement
Dentures
Root Canals
Updates

Just an FYI, I added an email address and website address.

I also added my Pic.  Please give designs with and without the pic

Thanks

Target Market(s)

20-70 U.S. Female that handles the household budget.

Industry/Entity Type

Dental

Requirements
Must have
• The logo is key. The color scheme of the logo is also key. The back of the business card should have the list of Dental Services offered at the practice. The front should be clean and professional looking. No cartoons. I will also include a picture of myself. I think that the final card may or may not include this picture, so the card designs should come with and without the picture. USE THE BLUE LOGO ONLY!!!
Should not have
• NO teeth should be on the card.

```html
<!DOCTYPE html>
<html lang="en">
<head>
<meta charset="utf-8">
<title>Halvorsen Dental Center – Business Cards</title>
<link rel="stylesheet" href="https://fonts.googleapis.com/css2?family=Lato:wght@400;700&display=swap">
<style>
  :root {
    --bg: #e6e4e1;
    --card: #ffffff;
    --blue: #5d89a6;
    --grey: #4e4e50;
    --rule: #6a6a6c;
    --shadow: rgba(0, 0, 0, 0.18);
  }
  * { margin: 0; padding: 0; box-sizing: border-box; }
  html, body {
    width: 1200px; height: 951px; overflow: hidden;
    background: var(--bg);
    font-family: "Lato", Arial, sans-serif;
    color: var(--grey);
  }
  .canvas { position: relative; width: 1200px; height: 951px; }
  .card {
    position: absolute;
    width: 620px; height: 354px;
    background: var(--card);
    border-radius: 22px;
    box-shadow: 0 10px 28px var(--shadow);
  }
  .card--back { left: 90px; top: 70px; }
  .card--front { left: 490px; top: 520px; }

  .brand { display: flex; align-items: center; gap: 14px; }
  .brand__dot { border-radius: 50%; background: var(--blue); flex: none; }
  .brand__name { color: var(--blue); font-weight: 400; line-height: 1.05; }

  .card--back .brand { position: absolute; left: 92px; top: 58px; }
  .card--back .brand__dot { width: 74px; height: 74px; }
  .card--back .brand__name { font-size: 40px; }

  .services {
    position: absolute; left: 0; right: 0; top: 230px;
    text-align: center; font-size: 19px; line-height: 1.32;
    color: var(--grey); letter-spacing: 0.3px;
  }

  .card--front .brand { position: absolute; left: 36px; top: 42px; gap: 10px; }
  .card--front .brand__dot { width: 50px; height: 50px; }
  .card--front .brand__name { font-size: 27px; }

  .rule { position: absolute; left: 36px; right: 36px; top: 150px; height: 1px; background: var(--rule); }
  .person { position: absolute; right: 40px; top: 160px; text-align: right; }
  .person__name { color: var(--blue); font-size: 22px; letter-spacing: 0.4px; }
  .person__title { font-size: 14px; margin-top: 2px; letter-spacing: 1px; }

  .contact { position: absolute; left: 30px; top: 244px; list-style: none; font-size: 14px; }
  .contact li { display: flex; align-items: center; gap: 10px; height: 22px; }
  .contact svg { width: 14px; height: 14px; flex: none; }
  .contact .web { color: var(--grey); }
  .contact .web span { color: var(--blue); }

  .address { position: absolute; right: 40px; top: 282px; text-align: right; font-size: 14px; line-height: 1.55; font-style: normal; }
</style>
</head>
<body>
<main class="canvas">
  <section class="card card--back" aria-label="Card back">
    <div class="brand">
      <span class="brand__dot"></span>
      <span class="brand__name">Halvorsen<br>Dental Center</span>
    </div>
    <p class="services">
      Family Dentistry • Cosmetic • Whitening<br>
      Tooth Colored Fillings • Crowns/Bridges<br>
      Implants/Tooth Replacement • Dentures • Root Canals
    </p>
  </section>

  <section class="card card--front" aria-label="Card front">
    <div class="brand">
      <span class="brand__dot"></span>
      <span class="brand__name">Halvorsen<br>Dental Center</span>
    </div>
    <div class="rule"></div>
    <div class="person">
      <p class="person__name">Martin K. Halvorsen</p>
      <p class="person__title">D.D.S.</p>
    </div>
    <ul class="contact">
      <li>
        <svg viewBox="0 0 14 14" aria-hidden="true"><circle cx="7" cy="7" r="6.5" fill="none" stroke="var(--blue)" stroke-width="1.2"/><path d="M5 4c-.8.6-.8 1.8 0 3.3s2 2.7 3 2.9l1-1-1.2-1-.7.5c-.6-.3-1.2-1-1.5-1.6l.5-.7-1-1.3z" fill="var(--blue)"/></svg>
        (719) 555-0186
      </li>
      <li>
        <svg viewBox="0 0 14 14" aria-hidden="true"><circle cx="7" cy="7" r="7" fill="var(--blue)"/><rect x="3.5" y="4.8" width="7" height="4.6" fill="#fff"/><path d="M3.5 4.8 7 7.6l3.5-2.8" fill="none" stroke="var(--blue)" stroke-width="0.8"/></svg>
        halvorsendentalcenter@mailnest.example
      </li>
      <li class="web">
        <svg viewBox="0 0 14 14" aria-hidden="true"><circle cx="7" cy="7" r="7" fill="var(--blue)"/></svg>
        <p>www.<span>halvorsendentalcenter</span>.example</p>
      </li>
    </ul>
    <address class="address">
      2847 Willow Bend Rd. Suite B<br>
      Colorado Springs, CO 80471
    </address>
  </section>
</main>
</body>
</html>
```